Stationery Design Project for Kow Lam Holdings

Kow Lam Holdings is a trading company originating in Hong Kong. We need full package of stationery designs that will include:

Business cards
Folder
Letter head
Envelopes large and small
Invoice
Packing list
Purchase order
Thank you card

All files shall be delivered in open source where the modification could be done.

Industry/Entity Type

Business

```html
<!DOCTYPE html>
<html lang="en">
<head>
<meta charset="utf-8">
<title>Kow Lam Holdings — Invoice</title>
<link rel="stylesheet" href="https://fonts.googleapis.com/css2?family=Open+Sans:wght@400;600;700;800&display=swap">
<style>
  :root {
    --bg: #e9e9e9;
    --paper: #fbfbfb;
    --ink: #2b2b2b;
    --rule: #6d6d6d;
    --label-fill: #d9d9d9;
    --band: #262626;
    --brand-green: #1f8a3a;
    --brand-orange: #f0a12a;
    --brand-yellow: #f2cc1c;
  }
  * { box-sizing: border-box; margin: 0; padding: 0; }
  html, body { width: 1200px; height: 960px; overflow: hidden; }
  body {
    background: var(--bg);
    font-family: "Open Sans", Arial, sans-serif;
    color: var(--ink);
    position: relative;
  }
  .invoice {
    position: absolute;
    left: 282px; top: 30px;
    width: 636px; height: 900px;
    background: var(--paper);
    box-shadow: 0 6px 18px rgba(0,0,0,.12);
    overflow: hidden;
  }
  .brand {
    position: absolute; left: 52px; top: 74px;
    display: flex; align-items: center; gap: 10px;
  }
  .brand-mark { width: 22px; height: 22px; background: var(--brand-orange); }
  .brand-name {
    font-weight: 800; font-size: 24px; letter-spacing: .5px;
    color: var(--brand-green); text-transform: uppercase; line-height: 1;
  }
  .address-block { position: absolute; font-size: 9px; line-height: 1.3; }
  .address-block h3 { font-size: 11px; font-weight: 700; }
  .job-site { left: 44px; top: 178px; }
  .contact { left: 372px; top: 108px; }

  .details {
    position: absolute; left: 40px; top: 246px; width: 556px;
    border: 1px solid var(--rule); border-radius: 8px; overflow: hidden;
    display: grid; grid-template-columns: 1fr 1fr 1fr 1fr;
  }
  .details .cell { border-right: 1px solid var(--rule); border-bottom: 1px solid var(--rule); text-align: center; }
  .details .cell:nth-child(4n) { border-right: none; }
  .details .row2 { border-bottom: none; }
  .details .label { background: var(--label-fill); font-size: 10px; font-weight: 700; padding: 2px 0; border-bottom: 1px solid var(--rule); }
  .details .value { font-size: 9px; padding: 2px 0 3px; }
  .details .wide { grid-column: span 2; }

  .items { position: absolute; left: 0; top: 0; }
  .col-head {
    position: absolute; top: 336px; height: 18px;
    font-size: 7px; color: #e6e6e6; text-transform: uppercase;
    text-align: center; line-height: 18px; letter-spacing: .3px;
  }
  .totals-label {
    position: absolute; left: 380px; width: 92px; text-align: right;
    font-size: 8px; text-transform: uppercase;
  }
  .footer-contact {
    position: absolute; left: 40px; right: 30px; top: 868px;
    display: flex; gap: 14px; align-items: center;
    font-size: 8px; color: #f2f2f2;
  }
  .footer-contact span { display: flex; align-items: center; gap: 4px; }
  .footer-contact svg { width: 9px; height: 9px; }
</style>
</head>
<body>
  <main class="invoice">
    <div class="brand">
      <span class="brand-mark"></span>
      <span class="brand-name">Kow Lam Holdings</span>
    </div>

    <section class="address-block contact">
      <h3>Contact:</h3>
      <p>Northwind Weaving</p>
      <p>G-204, Harbour Lane, Eastfield</p>
      <p>E.P.Z. 75710,</p>
    </section>

    <section class="address-block job-site">
      <h3>Job Site:</h3>
      <p>Northwind Weaving</p>
      <p>G-204, Harbour Lane, Eastfield</p>
      <p>E.P.Z. 75710,</p>
    </section>

    <section class="details">
      <div class="cell"><div class="label">Salesperson</div><div class="value">Mei</div></div>
      <div class="cell"><div class="label">Customer PO</div><div class="value">000000</div></div>
      <div class="cell wide"><div class="label">Payment Terms</div><div class="value">Net 60 Days</div></div>
      <div class="cell row2"><div class="label">Invoice #</div><div class="value">00000</div></div>
      <div class="cell row2"><div class="label">Job</div><div class="value">Door Repair</div></div>
      <div class="cell row2"><div class="label">Invoice Date</div><div class="value">4/29/11</div></div>
      <div class="cell row2"><div class="label">Due Date</div><div class="value">6/28/11</div></div>
    </section>

    <svg class="items" width="636" height="900" viewBox="0 0 636 900" aria-hidden="true">
      <path d="M40 344 Q40 336 48 336 L588 336 Q596 336 596 344 L596 354 L40 354 Z" fill="var(--band)"/>
      <path d="M40 354 L40 732 Q40 740 48 740 L362 740 Q370 740 370 732 L370 600 L588 600 Q596 600 596 592 L596 354"
            fill="none" stroke="var(--rule)" stroke-width="1"/>
      <line x1="100" y1="354" x2="100" y2="740" stroke="var(--rule)"/>
      <line x1="370" y1="354" x2="370" y2="600" stroke="var(--rule)"/>
      <line x1="480" y1="354" x2="480" y2="600" stroke="var(--rule)"/>
      <rect x="484" y="606" width="112" height="20" rx="10" fill="none" stroke="var(--rule)"/>
      <rect x="484" y="631" width="112" height="20" rx="10" fill="none" stroke="var(--rule)"/>
      <rect x="484" y="656" width="112" height="20" rx="10" fill="none" stroke="var(--rule)"/>

      <path d="M0 826 Q330 760 636 748 L636 900 L0 900 Z" fill="var(--band)"/>
      <path d="M0 818 Q330 752 636 740" fill="none" stroke="var(--brand-yellow)" stroke-width="5"/>
      <path d="M0 811 Q330 745 636 733" fill="none" stroke="var(--brand-orange)" stroke-width="1.5"/>
    </svg>

    <div class="col-head" style="left:40px;width:60px">Qty</div>
    <div class="col-head" style="left:100px;width:270px">Description</div>
    <div class="col-head" style="left:370px;width:110px">Unit Price</div>
    <div class="col-head" style="left:480px;width:116px">Line Total</div>

    <div class="totals-label" style="top:611px">Subtotal</div>
    <div class="totals-label" style="top:636px">Sales Tax</div>
    <div class="totals-label" style="top:661px">Total</div>

    <footer class="footer-contact">
      <span><svg viewBox="0 0 10 10"><circle cx="5" cy="5" r="5" fill="var(--brand-orange)"/><path d="M5 2.2a1.8 1.8 0 0 0-1.8 1.8C3.2 5.4 5 7.8 5 7.8S6.8 5.4 6.8 4A1.8 1.8 0 0 0 5 2.2z" fill="#fff"/></svg>Kadestraat 22-B4, 5678 CD, Zwolle</span>
      <span><svg viewBox="0 0 10 10"><circle cx="5" cy="5" r="5" fill="var(--brand-orange)"/><path d="M3.2 2.5l1 .2.4 1.2-.6.5a3.5 3.5 0 0 0 1.6 1.6l.5-.6 1.2.4.2 1a.6.6 0 0 1-.6.6A4.6 4.6 0 0 1 2.6 3.1a.6.6 0 0 1 .6-.6z" fill="#fff"/></svg>415-555-0140</span>
      <span><svg viewBox="0 0 10 10"><circle cx="5" cy="5" r="5" fill="var(--brand-orange)"/><rect x="3" y="2.8" width="4" height="4.4" rx=".4" fill="#fff"/></svg>415-555-0147</span>
      <span><svg viewBox="0 0 10 10"><circle cx="5" cy="5" r="5" fill="var(--brand-orange)"/><rect x="2.6" y="3.3" width="4.8" height="3.4" fill="#fff"/><path d="M2.6 3.3L5 5.2l2.4-1.9" fill="none" stroke="var(--brand-orange)" stroke-width=".6"/></svg>info@kowlam.com</span>
      <span><svg viewBox="0 0 10 10"><circle cx="5" cy="5" r="5" fill="var(--brand-orange)"/><circle cx="5" cy="5" r="2.4" fill="none" stroke="#fff" stroke-width=".8"/><line x1="2.6" y1="5" x2="7.4" y2="5" stroke="#fff" stroke-width=".6"/></svg>www.kowlam.com</span>
    </footer>
  </main>
</body>
</html>
```